Covid19 Poster for workplaces

Create a poster on how to protect yourself from Corona virus at work.
We are a Calmfield Wellness company. We have just re-branded so we need to fit in with our brand. We like clean and fresh, slightly amusing is ok if it will draw attention but it's an important topic. A4 and A3 please.

Content:

Headline: Lower the risk of COVID 19 in the workplace.

BE WELL

Bring your own cup - don’t share cups and food.
Elbow tap instead of handshakes and kisses
Wash your hands often - with soap.
Elbow or tissues when you cough or sneeze then straight in the bin
Leave your face alone after touching shared surfaces
Leave your bugs at home if you’re feeling unwell.

Call health line if you have a cough, a high temperature and shortness of breath. 0800 472 9160

Based on recommendations from ZPK and QLN

Target Market(s)

Employees - so anyone

Other font styles liked:
• Use the closest font to the brand documents

Requirements
Should not have
• Clip art

```html
<!DOCTYPE html>
<html lang="en">
<head>
<meta charset="utf-8">
<title>Lower the risk of COVID19 in the workplace</title>
<link href="https://fonts.googleapis.com/css2?family=Arimo:wght@400;700&display=swap" rel="stylesheet">
<style>
  :root {
    --mint: #43e5b1;
    --ink: #000000;
    --paper: #ffffff;
  }
  html, body {
    margin: 0;
    padding: 0;
    overflow: hidden;
    background: var(--paper);
  }
  .poster {
    position: relative;
    width: 849px;
    height: 1200px;
    overflow: hidden;
    background: var(--paper);
    font-family: "Arimo", "Helvetica Neue", Arial, sans-serif;
    color: var(--ink);
  }
  .headline {
    position: absolute;
    left: 47px;
    top: 46px;
    margin: 0;
    font-size: 64px;
    font-weight: 700;
    line-height: 71px;
    letter-spacing: -0.5px;
  }
  .headline .accent { color: var(--mint); }
  .slogan {
    position: absolute;
    left: 54px;
    top: 228px;
    margin: 0;
    font-size: 100px;
    font-weight: 400;
    line-height: 100px;
    letter-spacing: -2px;
    color: var(--mint);
  }
  .brand {
    position: absolute;
    left: 600px;
    top: 272px;
    display: flex;
    align-items: center;
    gap: 12px;
  }
  .brand-dot {
    width: 30px;
    height: 30px;
    border-radius: 50%;
    background: var(--mint);
  }
  .brand-name {
    font-size: 23px;
    font-weight: 700;
    line-height: 25px;
    color: var(--ink);
  }
  .tips-band {
    position: absolute;
    left: 0;
    top: 332px;
    width: 849px;
    height: 672px;
    background: var(--mint);
  }
  .tips {
    list-style: none;
    margin: 0;
    padding: 0;
    position: absolute;
    left: 111px;
    top: 77px;
    width: 680px;
    color: var(--paper);
    font-size: 34px;
    font-weight: 700;
    line-height: 36px;
  }
  .tips li {
    position: relative;
    margin-bottom: 22px;
  }
  .tips li::before {
    content: "";
    position: absolute;
    left: -18px;
    top: 15px;
    width: 9px;
    height: 9px;
    border-radius: 50%;
    background: var(--paper);
  }
  .health-line {
    position: absolute;
    left: 57px;
    top: 1013px;
    width: 760px;
    margin: 0;
    font-size: 21.5px;
    line-height: 29px;
    font-weight: 400;
  }
  .source {
    position: absolute;
    left: 57px;
    top: 1116px;
    margin: 0;
    font-size: 27px;
    font-weight: 700;
    color: var(--mint);
  }
</style>
</head>
<body>
<main class="poster">
  <h1 class="headline">Lower the risk of <span class="accent">COVID19</span><br>in the workplace.</h1>
  <p class="slogan">BE WELL</p>
  <div class="brand">
    <span class="brand-dot"></span>
    <span class="brand-name">Calmfield<br>Wellness</span>
  </div>
  <section class="tips-band">
    <ul class="tips">
      <li>Bring your own cup - don’t share cups and food.</li>
      <li>Elbow tap instead of handshakes and kisses</li>
      <li>Wash your hands often - with soap.</li>
      <li>Elbow or tissues when you cough or sneeze then straight in the bin</li>
      <li>Leave your face alone after touching shared surfaces</li>
      <li>Leave your bugs at home if you’re feeling unwell.</li>
    </ul>
  </section>
  <p class="health-line">Call health line if you have a cough, a high temperature and shortness of breath. 0800 472 9160</p>
  <p class="source">Based on recommendations from ZPK and QLN</p>
</main>
</body>
</html>
```